Plumcast Web Design

We require the design of 3 pages for our Plumcast website. We have designed a general layout, which you can see at the link below:

https://files.plovari.com/folder/d/7QmZ204kwPtEcLsRRuMoPiWxYtV2/edit?usp=sharing

We need you to design the colour scheme, detailed layout and graphics. We will provide you with three basic HTML pages that will contain text and we would like you to return completed .css files. The html files are only to make your job simpler and to provide details. If it is easier for you to build the .css files from scratch then it is not necessary for you to use them. Also, if you would like to edit the html files feel free. We would like you to focus on the creative design component, specifically colours and graphics.

In terms of colours, we would like to avoid red and blue. We would also prefer not to have various shades of black and dark grey. We like strong, simple design colours that are easy on the eye.
**Update on Colour Themes**
Apologies, I feel that I wasn't entirely clear about the colours, specifically red, blue and black. We'd prefer to stay away from the use of red and blue as a major components of the theme. It is already used quite heavily in other Plumcast sites and we're after a distinct look of our own. I didn't mean to suggest that no red or blue can be used in the design.
***

Some websites that we like the look of include:
https://velmora.com - We particularly like the layout and the colour scheme and contrasts. We would however, prefer to avoid blue themes.
www.brondiva.com
www.kaluthen.com
www.trepavine.com - The icons, images and style of this site are really good. As stated above, we'd prefer to avoid black though.

There is no need to design a primary website logo, but please design other icons, buttons and graphics.

We would prefer the page to be bold, modern and fun rather than professional. In addition, we like clean, uncluttered designs and designs that emphasize user experience. The Homepage listed is quite empty in terms of content, so you have freedom to be particularly creative on this page.

If you have any further questions please ask, we are very happy to provide any further details or help you might need.
Updates

Thanks in advance.

Target Market(s)

Plumcast users

Industry/Entity Type

Media

Requirements
Must have
• We require css files at the end of the project.
We require the creation of every field in the design document to complete the project.
The spacial layout must replicate the design document.
Should not have
• Flash, Quarrendeck

```html
<!DOCTYPE html>
<html lang="en">
<head>
<meta charset="utf-8">
<title>Plumcast – Home</title>
<link rel="stylesheet" href="https://fonts.googleapis.com/css2?family=Mulish:wght@300;400;600;700&family=Arimo:wght@400;700&display=swap">
<style>
  :root {
    --purple: #7d0aa3;
    --purple-dark: #5f0380;
    --purple-light: #9a1cc6;
    --ink: #3d3d3d;
    --muted: #9a9a9a;
    --panel-border: #c9c9c9;
    --field-border: #c4c4c4;
    --button-dark: #3a3a3a;
    --tab-dark: #262626;
    --white: #ffffff;
    --lang-blue: #2a7cc7;
    --footer-text: #e3c6ef;
  }
  * { box-sizing: border-box; margin: 0; padding: 0; }
  html, body { width: 1200px; height: 614px; overflow: hidden; }
  body {
    position: relative;
    font-family: "Mulish", sans-serif;
    color: var(--ink);
    background: var(--white);
  }
  .backdrop {
    position: absolute; left: 0; top: 43px; width: 1200px; height: 526px;
    background:
      radial-gradient(ellipse at 20% 40%, #f1f1f1 0%, transparent 55%),
      radial-gradient(ellipse at 85% 70%, #eeeeee 0%, transparent 50%),
      linear-gradient(180deg, #f9f9f9 0%, #f3f3f3 100%);
  }
  .topbar {
    position: absolute; left: 0; top: 0; width: 1200px; height: 43px;
    background: linear-gradient(180deg, var(--purple-light) 0%, var(--purple) 60%, var(--purple-dark) 100%);
  }
  .brand {
    position: absolute; left: 198px; top: 0; height: 43px; line-height: 43px;
    font-size: 24px; font-weight: 600; color: var(--white);
  }
  .nav { position: absolute; left: 386px; top: 0; height: 43px; display: flex; }
  .nav a {
    display: block; height: 43px; line-height: 43px; padding: 0 14px;
    color: var(--white); font-size: 14px; font-weight: 600; text-decoration: none;
  }
  .nav a + a { margin-left: 8px; }
  .nav a.is-active { background: var(--tab-dark); }
  .search {
    position: absolute; left: 806px; top: 10px; width: 192px; height: 26px;
    background: var(--white); border: 1px solid #d8d8d8; border-radius: 3px;
    font-family: "Arimo", sans-serif; font-size: 11px; color: #b5b5b5;
    padding-left: 9px; line-height: 24px;
  }
  .hero { position: absolute; left: 200px; top: 80px; }
  .hero h1 { font-size: 42px; font-weight: 300; line-height: 52px; color: var(--ink); white-space: nowrap; }
  .hero h1 strong { color: var(--purple); font-weight: 700; }
  .hero p { margin-top: 6px; width: 370px; font-size: 14px; font-weight: 300; line-height: 17px; color: #4a4a4a; }
  .join {
    display: inline-block; margin-top: 10px; width: 132px; height: 39px; line-height: 39px;
    text-align: center; border-radius: 3px; color: var(--white);
    font-size: 19px; font-weight: 600;
    background: linear-gradient(180deg, var(--purple-light) 0%, var(--purple-dark) 100%);
  }
  .panel {
    position: absolute; left: 744px; width: 258px;
    background: linear-gradient(180deg, #fbfbfb 0%, #eeeeee 100%);
    border: 1px solid var(--panel-border); border-radius: 3px;
    box-shadow: 0 2px 4px rgba(0,0,0,0.22);
    padding: 15px 12px 0 15px;
  }
  .panel--login { top: 76px; height: 177px; }
  .panel--signup { top: 269px; height: 212px; }
  .panel h2 { font-size: 19px; font-weight: 600; color: var(--purple); line-height: 22px; margin-bottom: 11px; }
  .field {
    position: relative; width: 230px; height: 32px; margin-bottom: 8px;
    background: var(--white); border: 1px solid var(--field-border); border-radius: 3px;
    font-family: "Arimo", sans-serif; font-size: 11px; color: #a8a8a8;
    line-height: 30px; padding-left: 35px;
  }
  .field svg { position: absolute; left: 9px; top: 8px; width: 14px; height: 14px; }
  .panel__actions { display: flex; justify-content: space-between; align-items: center; width: 230px; margin-top: 2px; }
  .forgot { font-family: "Arimo", sans-serif; font-size: 9.5px; color: #333; text-decoration: underline; }
  .btn-dark {
    width: 79px; height: 26px; line-height: 24px; text-align: center;
    background: linear-gradient(180deg, #555 0%, var(--button-dark) 100%);
    border: 1px solid #222; border-radius: 3px;
    color: var(--white); font-size: 14px; font-weight: 600;
  }
  .language { position: absolute; left: 891px; top: 534px; display: flex; align-items: center; gap: 6px; font-family: "Arimo", sans-serif; font-size: 10px; color: var(--muted); }
  .language__pick {
    display: flex; align-items: center; gap: 4px; width: 53px; height: 17px; padding-left: 5px;
    background: var(--lang-blue); border-radius: 2px; color: var(--white); font-weight: 700; font-size: 9px;
  }
  .footer {
    position: absolute; left: 0; top: 569px; width: 1200px; height: 45px;
    background: linear-gradient(180deg, var(--purple) 0%, var(--purple-dark) 100%);
    font-family: "Arimo", sans-serif; font-size: 8.5px; color: var(--footer-text);
  }
  .footer__copy { position: absolute; left: 201px; top: 17px; }
  .footer__links { position: absolute; right: 201px; top: 17px; }
  .footer__links span { margin: 0 4px; }
</style>
</head>
<body>
  <div class="backdrop" role="img" aria-label="Faint illustrated network of desktop computers linked by lines"></div>

  <header class="topbar">
    <div class="brand">Plumcast</div>
    <nav class="nav">
      <a class="is-active" href="#">Home</a>
      <a href="#">People</a>
      <a href="#">Explore</a>
    </nav>
    <div class="search">Search</div>
  </header>

  <section class="hero">
    <h1>Welcome to <strong>Plumcast</strong></h1>
    <p>Duis quam sapien, condimentum ac imperdiet sit amet, ornare et eros. Quisque venenatis molestie arcu aliquet imperdiet. Aliquam erat volutpat.</p>
    <a class="join">JOIN NOW</a>
  </section>

  <section class="panel panel--login">
    <h2>LOGIN</h2>
    <div class="field">
      <svg viewBox="0 0 14 14"><circle cx="7" cy="4" r="3" fill="#c8c8c8"/><path d="M1 14c0-4 3-6 6-6s6 2 6 6z" fill="#c8c8c8"/></svg>
      Username
    </div>
    <div class="field">
      <svg viewBox="0 0 14 14"><circle cx="4" cy="10" r="3.5" fill="#c8c8c8"/><path d="M6 8l7-7" stroke="#c8c8c8" stroke-width="2"/></svg>
      Password
    </div>
    <div class="panel__actions">
      <span class="forgot">Forgot Password</span>
      <span class="btn-dark">LOGIN</span>
    </div>
  </section>

  <section class="panel panel--signup">
    <h2>SIGN UP</h2>
    <div class="field">
      <svg viewBox="0 0 14 14"><rect x="0" y="3" width="14" height="9" fill="#c8c8c8"/><path d="M0 3l7 5 7-5" stroke="#fff" fill="none"/></svg>
      Register Email
    </div>
    <div class="field">
      <svg viewBox="0 0 14 14"><circle cx="4" cy="10" r="3.5" fill="#c8c8c8"/><path d="M6 8l7-7" stroke="#c8c8c8" stroke-width="2"/></svg>
      Password
    </div>
    <div class="field">
      <svg viewBox="0 0 14 14"><circle cx="4" cy="10" r="3.5" fill="#c8c8c8"/><path d="M6 8l7-7" stroke="#c8c8c8" stroke-width="2"/></svg>
      Confirm Password
    </div>
    <div class="panel__actions">
      <span class="forgot">Forgot Password</span>
      <span class="btn-dark">LOGIN</span>
    </div>
  </section>

  <div class="language">
    Language:
    <span class="language__pick">EN
      <svg width="13" height="9" viewBox="0 0 13 9"><rect width="13" height="9" fill="#fff"/><rect y="0" width="13" height="1.3" fill="#d44"/><rect y="2.6" width="13" height="1.3" fill="#d44"/><rect y="5.2" width="13" height="1.3" fill="#d44"/><rect y="7.8" width="13" height="1.2" fill="#d44"/><rect width="6" height="4.5" fill="#3a4f9a"/></svg>
      <svg width="8" height="5" viewBox="0 0 8 5"><path d="M0 0h8L4 5z" fill="#fff"/></svg>
    </span>
  </div>

  <footer class="footer">
    <div class="footer__copy">© 2013 Plumcast. All Rights Reserved.</div>
    <div class="footer__links">About<span>|</span>Terms of use<span>|</span>Confidentiality</div>
  </footer>
</body>
</html>
```